Would like a website to blog, vlog and post pictures about a upcoming glowtrek road trip in a 1977 KX VAN.
We will have custom bumper stickers available (by donation or a set amount - unsure) and would like to be able mail these out in the future.
Would like the website to be easy to use, simple. clean with a modern hippie/boho feel.
The travelling van is original green. We have a custom lic plate 'glowtrek'
The stickers are black, white and red.
Our mission:
A Love movement journey to raise the vibration and awareness of Boundless Glow.
We plan to have it painted with washable paint at certain spots along the way. We will ask willing people to make a journal entry of how they glowtrek (spread the love) and I will quote them in my blog or blog.
The picture attached is me, Dorinda after we painted "Breezy" (the van's given name) with friends for a Canada Day celebration.
The road trip is with my boyfriend and our two 13yr olds - a boy and a girl.
However, the road trip in August is just the beginning of what I envision to be a much longer journey...so I would like the website created to hold space for future adventures :)
Happy creating to whomever feels their heart strings pulled to be part of our glowtrek journey!
With Love and Gratitude,
Dorinda (Band of Sunrise:)
Please note:
KX pic is for inspiration only - please do not use it on the site. Thank you.

Industry/Entity Type

Paint

Requirements
Must have
• Opt in for Future Newsletter, blog, vlog, join the movement - permission to get creative ;)
Email: dorinda@glowtrek.example

```html
<!DOCTYPE html>
<html lang="en">
<head>
<meta charset="utf-8">
<title>Glowtrek – Road Trip</title>
<link href="https://fonts.googleapis.com/css2?family=Open+Sans:ital,wght@0,400;0,600;1,400;1,600&family=Roboto+Condensed:wght@300;400&display=swap" rel="stylesheet">
<style>
:root{
  --black:#050505;
  --red:#d50f0f;
  --red-dark:#b70b0b;
  --grey-btn:#5a5a5a;
  --page:#ebe9ea;
  --green:#95b466;
  --white:#ffffff;
  --text:#666;
  --dark:#222;
}
*{margin:0;padding:0;box-sizing:border-box}
html,body{width:786px;height:1200px;overflow:hidden}
body{position:relative;background:var(--page);font-family:"Open Sans",sans-serif;color:var(--text)}
.abs{position:absolute}
h1,h2,h3{font-weight:400}

/* header */
.site-header{left:0;top:0;width:786px;height:77px;background:var(--black)}
.brand{left:82px;top:16px;color:var(--white);font-family:"Roboto Condensed",sans-serif;font-weight:400;font-size:30px;letter-spacing:1px;display:flex;align-items:center;gap:6px}
.brand-dot{width:12px;height:12px;border-radius:50%;background:var(--red)}
.brand-domain{left:116px;top:50px;color:var(--white);font-size:9px;font-weight:600;letter-spacing:1px}
.social{left:592px;top:14px;display:flex;gap:5px}
.social span{width:20px;height:20px;border-radius:50%;border:1.5px solid #777}
.social span:first-child{background:#3a5a9a;border-color:#3a5a9a}
.nav{top:52px;height:25px;color:#eee;font-family:"Roboto Condensed",sans-serif;font-size:11px;display:flex;align-items:center;justify-content:center;background:var(--grey-btn);border-top:1px solid #777}
.nav.active{background:var(--red);border-top-color:#f33;color:#fff}

/* hero */
.band{left:0;top:77px;width:786px;height:201px;background:var(--green)}
.hero{left:79px;top:104px;width:628px;height:262px;background:linear-gradient(160deg,#9a7a50 0%,#c9a36a 25%,#5a5a55 45%,#3e3e3c 75%,#2b2b2a 100%);border:1px solid #fff}
.hero-title{left:166px;top:292px;color:#fff;font-family:"Roboto Condensed",sans-serif;font-weight:300;font-size:47px;letter-spacing:-1px;white-space:nowrap}
.dots{left:634px;top:340px;display:flex;gap:6px}
.dots span{width:10px;height:10px;border-radius:50%;background:#111;color:#fff;font-size:5px;text-align:center;line-height:10px}
.dots span:first-child{background:var(--red)}

/* posts */
.post{left:79px;width:426px;height:237px;background:var(--white);border-bottom:2px solid #cfcdce}
.post-photo{position:absolute;left:0;top:0;width:212px;height:237px}
.post-title{position:absolute;left:225px;top:10px;width:195px;color:var(--red);font-size:10px;white-space:nowrap}
.post-date{position:absolute;left:225px;top:29px;color:var(--dark);font-size:8px;font-style:italic;font-weight:600;white-space:nowrap}
.post-text{position:absolute;left:225px;top:50px;width:188px;font-size:6.9px;line-height:13.8px;text-align:justify;letter-spacing:-0.05px}
.btn-more{position:absolute;left:226px;top:198px;width:67px;height:21px;background:var(--red);color:#fff;font-size:8.5px;font-style:italic;font-weight:600;display:flex;align-items:center;justify-content:center}

/* sidebar */
.video{left:530px;top:398px;width:177px;height:99px;background:linear-gradient(180deg,#3a302c,#1a1512 60%,#0d0a08)}
.search{left:530px;top:518px;width:146px;height:27px;background:#fff;border:1px solid #d8d8d8;font-size:8px;font-style:italic;color:#aaa;padding:8px 8px}
.go{left:675px;top:518px;width:32px;height:27px;background:var(--red);color:#fff;font-size:10px;font-weight:600;display:flex;align-items:center;justify-content:center}
.side-h{left:530px;color:var(--red);font-family:"Roboto Condensed",sans-serif;font-size:14px;white-space:nowrap}
.rule{left:530px;width:177px;height:1px;background:var(--red)}
.event{left:530px;width:177px;height:57px;background:#fff}
.event-photo{position:absolute;top:0;width:82px;height:57px}
.event-info{position:absolute;top:8px;white-space:nowrap}
.event-date{font-size:8px;font-style:italic;font-weight:600;color:var(--dark)}
.event-title{font-size:9px;color:var(--red);margin-top:3px}
.event-more{font-size:7.5px;font-style:italic;color:#888;margin-top:3px}
.story{left:530px;top:853px;width:177px;height:99px;background:linear-gradient(120deg,#9fb3c2,#e6d5c6 50%,#5a6e7c)}
.news-text{left:530px;top:999px;width:177px;font-size:8.3px;line-height:15px}
.email-icon{left:530px;top:1035px;width:36px;height:25px;background:#ddd}
.email{left:566px;top:1035px;width:113px;height:25px;background:#fff;border:1px solid #ddd;font-size:8px;font-style:italic;color:#aaa;padding:6px 6px}
.send{left:679px;top:1035px;width:28px;height:25px;background:var(--red)}
.join{left:530px;top:1081px;width:177px;height:71px;background:linear-gradient(90deg,#7a6a55,#4a3e33 50%,#2a2420)}
.join-text{left:610px;top:1088px;color:#fff;font-family:"Roboto Condensed",sans-serif;font-size:16px;line-height:19px}
.join-more{left:672px;top:1134px;width:35px;height:18px;background:var(--red);color:#fff;font-size:8px;display:flex;align-items:center;justify-content:center}

/* footer */
.footer{left:0;top:1170px;width:786px;height:30px;background:var(--black);font-size:8.3px;color:#999}
.footer-nav{position:absolute;left:79px;top:9px;white-space:nowrap}
.footer-nav b{color:#fff;font-weight:600}
.copy{position:absolute;right:79px;top:9px;white-space:nowrap}
</style>
</head>
<body>

<header class="abs site-header">
  <div class="abs brand">GLOWTREK<span class="brand-dot"></span></div>
  <div class="abs brand-domain">GLOWTREK.EXAMPLE</div>
  <div class="abs social"><span></span><span></span><span></span><span></span><span></span></div>
  <nav>
    <a class="abs nav active" style="left:310px;width:48px">HOME</a>
    <a class="abs nav" style="left:366px;width:64px">ABOUT US</a>
    <a class="abs nav" style="left:440px;width:61px">SERVICES</a>
    <a class="abs nav" style="left:511px;width:54px">KX VAN</a>
    <a class="abs nav" style="left:575px;width:46px">BLOG</a>
    <a class="abs nav" style="left:630px;width:72px">CONTACT US</a>
  </nav>
</header>

<div class="abs band" role="img" aria-label="Green damask pattern band"></div>
<div class="abs hero" role="img" aria-label="Open road curving past rocky hills at sunset"></div>
<h1 class="abs hero-title">ROAD TRIP CANANDA</h1>
<div class="abs dots"><span>1</span><span>2</span><span>3</span></div>

<article class="abs post" style="top:398px">
  <div class="post-photo" role="img" aria-label="Two friends riding in a convertible" style="background:linear-gradient(135deg,#7d9a4a,#c9b07a 50%,#4a5a3a)"></div>
  <h2 class="post-title">Lorem ipsum dolor sit amet consectetur</h2>
  <p class="post-date">Monday, &nbsp;&nbsp;21 - Jul - 2014</p>
  <p class="post-text">Lorem ipsum dolor sit amet, consectetur adipiscing elit. Quisque id velit sed tellus laoreet facilisis quis at nunc. Suspendisse non tempor leo. Vestibulum dolor nulla, ultricies et eros sit amet, congue ullamcorper leo. Interdum et malesuada fames ac ante ipsum primis in faucibus. Aenean id mauris aliquam, molestie tellus eu, facilisis quam. Mauris semper, justo eget sodales venenatis, dui orci convallis elit, at rhoncus sem elit in est. Praesent lacinia placerat metus,</p>
  <a class="btn-more">Read more</a>
</article>

<article class="abs post" style="top:656px">
  <div class="post-photo" role="img" aria-label="Woman in a sun hat beside a vintage car" style="background:linear-gradient(135deg,#d8c9a8,#8a7a5a 50%,#2a2520)"></div>
  <h2 class="post-title">Lorem ipsum dolor sit amet consectetur</h2>
  <p class="post-date">Monday, &nbsp;&nbsp;21 - Jul - 2014</p>
  <p class="post-text">Lorem ipsum dolor sit amet, consectetur adipiscing elit. Quisque id velit sed tellus laoreet facilisis quis at nunc. Suspendisse non tempor leo. Vestibulum dolor nulla, ultricies et eros sit amet, congue ullamcorper leo. Interdum et malesuada fames ac ante ipsum primis in faucibus. Aenean id mauris aliquam, molestie tellus eu, facilisis quam. Mauris semper, justo eget sodales venenatis, dui orci convallis elit, at rhoncus sem elit in est. Praesent lacinia placerat metus,</p>
  <a class="btn-more">Read more</a>
</article>

<article class="abs post" style="top:913px">
  <div class="post-photo" role="img" aria-label="Couple leaning out of a red car" style="background:linear-gradient(135deg,#9ab0a0,#d8204a 45%,#b01030)"></div>
  <h2 class="post-title">Lorem ipsum dolor sit amet consectetur</h2>
  <p class="post-date">Monday, &nbsp;&nbsp;21 - Jul - 2014</p>
  <p class="post-text">Lorem ipsum dolor sit amet, consectetur adipiscing elit. Quisque id velit sed tellus laoreet facilisis quis at nunc. Suspendisse non tempor leo. Vestibulum dolor nulla, ultricies et eros sit amet, congue ullamcorper leo. Interdum et malesuada fames ac ante ipsum primis in faucibus. Aenean id mauris aliquam, molestie tellus eu, facilisis quam. Mauris semper, justo eget sodales venenatis, dui orci convallis elit, at rhoncus sem elit in est. Praesent lacinia placerat metus,</p>
  <a class="btn-more">Read more</a>
</article>

<aside>
  <div class="abs video" role="img" aria-label="Video still of a car dashboard in the rain"></div>
  <svg class="abs" style="left:607px;top:432px" width="32" height="32" viewBox="0 0 32 32"><circle cx="16" cy="16" r="14" fill="none" stroke="#fff" stroke-width="2"/><path d="M13 10l9 6-9 6z" fill="#fff"/></svg>

  <div class="abs search">Search...</div>
  <div class="abs go">GO</div>

  <h3 class="abs side-h" style="top:558px">Latest Events</h3>

  <div class="abs event" style="top:580px">
    <div class="event-photo" style="left:0;background:linear-gradient(135deg,#7d9a4a,#c9b07a)" role="img" aria-label="Friends in a convertible"></div>
    <div class="event-info" style="left:90px"><p class="event-date">JUL 10, 2014</p><p class="event-title">Lorem ispum dolor</p><p class="event-more">Read more</p></div>
  </div>
  <div class="abs event" style="top:638px">
    <div class="event-info" style="left:7px"><p class="event-date">JUL 10, 2014</p><p class="event-title">Lorem ispum dolor</p><p class="event-more">Read more</p></div>
    <div class="event-photo" style="left:95px;background:linear-gradient(135deg,#d8c9a8,#6a5a45)" role="img" aria-label="Woman in a sun hat"></div>
  </div>
  <div class="abs event" style="top:696px">
    <div class="event-info" style="left:7px"><p class="event-date">JUL 10, 2014</p><p class="event-title">Lorem ispum dolor</p><p class="event-more">Read more</p></div>
    <div class="event-photo" style="left:95px;background:linear-gradient(135deg,#c01a3a,#8aa0b0)" role="img" aria-label="Woman smiling from a car window"></div>
  </div>
  <div class="abs event" style="top:755px">
    <div class="event-info" style="left:7px"><p class="event-date">JUL 10, 2014</p><p class="event-title">Lorem ispum dolor</p><p class="event-more">Read more</p></div>
    <div class="event-photo" style="left:95px;background:linear-gradient(135deg,#9ab0a0,#d8204a)" role="img" aria-label="Man leaning out of a red car"></div>
  </div>

  <h3 class="abs side-h" style="top:824px">Top Stories</h3>
  <div class="abs rule" style="top:845px"></div>
  <svg class="abs" style="left:684px;top:830px" width="23" height="15" viewBox="0 0 23 15"><path d="M0 15L12 0 23 15z" fill="var(--red)"/><circle cx="12" cy="10" r="2.5" fill="none" stroke="#fff" stroke-width="1"/></svg>
  <div class="abs story" role="img" aria-label="Man in a car holding up keys"></div>

  <h3 class="abs side-h" style="top:970px">Sign up newsletter</h3>
  <div class="abs rule" style="top:991px"></div>
  <p class="abs news-text">Lorem ipsum dolor sit amet, conctetur adipiscing elit quisque id velit</p>
  <svg class="abs email-icon" width="36" height="25" viewBox="0 0 36 25"><rect x="3" y="4" width="30" height="17" fill="#fff" stroke="#bbb"/><path d="M3 4l15 10 15-10" fill="none" stroke="#bbb"/></svg>
  <div class="abs email">your email...</div>
  <svg class="abs send" width="28" height="25" viewBox="0 0 28 25"><rect width="28" height="25" fill="var(--red)"/><path d="M8 6l13 6.5-13 6.5 3-6.5z" fill="#fff"/></svg>

  <div class="abs join" role="img" aria-label="Woman in a sun hat beside a vintage car"></div>
  <p class="abs join-text">JOIN THE<br>MOVEMENT</p>
  <a class="abs join-more">MORE</a>
</aside>

<footer class="abs footer">
  <div class="footer-nav"><b>Home</b> &nbsp;|&nbsp; About Us &nbsp;|&nbsp; Services &nbsp;|&nbsp; KX Van &nbsp;|&nbsp; Blog &nbsp;|&nbsp; Contact Us</div>
  <div class="copy">Copyright © 2014 glowtrek. All Rights Reserved</div>
</footer>

</body>
</html>
```